Australian Civil Construction, Quarry & Mining Services needs a business card

We need a business card designed for our Civil Construction, Quarry & Mining Services based in the country in Australia.
Our Company Brackley Earthworks provide innovate solutions for infrastructure, agricultural and mining (aggregate, sand, roadbase) industry.
We would like our business cards to be double sided
Front of card: black background or something that resembles our business colours. (it doesn't have to be black we are open to options)
- Company name - Brackley Earthworks
- Either our logo or some sort of icon/picture that resembles our business
- Website - https://brackleyearthworks.com.au/
- We will have a number of different names, positions descriptions, phone numbers and emails on separate cards for each of our managers/directors

```html
<!DOCTYPE html>
<html lang="en">
<head>
<meta charset="utf-8">
<title>Brackley Earthworks — Business Card</title>
<link rel="stylesheet" href="https://fonts.googleapis.com/css2?family=Michroma&family=Open+Sans:wght@400;600&family=Rajdhani:wght@700&display=swap">
<style>
  :root {
    --bg: #d6d6d6;
    --card: #1d1d1e;
    --card-edge: #2a2a2b;
    --orange: #f07d0f;
    --white: #f2f2f2;
    --grey-text: #dcdcdc;
  }
  * { box-sizing: border-box; margin: 0; padding: 0; }
  html, body { width: 1200px; height: 800px; overflow: hidden; }
  body {
    background: var(--bg);
    display: flex;
    align-items: center;
    justify-content: center;
    gap: 44px;
  }
  .card {
    position: relative;
    width: 540px;
    height: 309px;
    background: var(--card);
    border-radius: 20px;
    overflow: hidden;
    box-shadow: 0 14px 30px rgba(0,0,0,0.28);
  }

  /* Front side */
  .brand {
    position: absolute;
    top: 104px;
    left: 0;
    right: 0;
    display: flex;
    align-items: center;
    justify-content: center;
    gap: 14px;
  }
  .brand-square {
    width: 26px;
    height: 26px;
    background: var(--orange);
  }
  .brand-name {
    font-family: "Michroma", sans-serif;
    font-size: 19px;
    letter-spacing: 2px;
    color: var(--orange);
    text-transform: uppercase;
  }
  .website {
    position: absolute;
    left: 0;
    right: 0;
    bottom: 70px;
    text-align: center;
    font-family: "Michroma", sans-serif;
    font-size: 13px;
    letter-spacing: 3px;
    color: var(--orange);
  }
  .stripe {
    position: absolute;
    left: 0;
    right: 0;
    bottom: 28px;
    height: 30px;
    background: var(--orange);
  }

  /* Back side */
  .corner-mark {
    position: absolute;
    top: 0;
    right: 58px;
    width: 0;
    height: 0;
    border-left: 22px solid transparent;
    border-right: 22px solid transparent;
    border-top: 24px solid var(--orange);
  }
  .contact {
    position: absolute;
    top: 44px;
    right: 40px;
    text-align: right;
  }
  .person-name {
    font-family: "Rajdhani", sans-serif;
    font-weight: 700;
    font-size: 36px;
    line-height: 1;
    color: var(--white);
    text-transform: uppercase;
    letter-spacing: 0.5px;
  }
  .person-role {
    font-family: "Open Sans", sans-serif;
    font-size: 14px;
    color: var(--orange);
    margin: 4px 0 14px;
  }
  .contact-list { list-style: none; }
  .contact-list li {
    display: flex;
    align-items: center;
    justify-content: flex-end;
    gap: 9px;
    font-family: "Open Sans", sans-serif;
    font-size: 12.5px;
    line-height: 1.55;
    color: var(--grey-text);
  }
  .contact-list svg { width: 12px; height: 12px; flex: none; }
  .contact-list .no-icon { padding-right: 21px; }
</style>
</head>
<body>

  <section class="card card-front" aria-label="Business card front">
    <div class="brand">
      <span class="brand-square"></span>
      <span class="brand-name">Brackley Earthworks</span>
    </div>
    <p class="website">WWW.BRACKLEYEARTHWORKS.COM.AU</p>
    <div class="stripe"></div>
  </section>

  <section class="card card-back" aria-label="Business card back">
    <span class="corner-mark"></span>
    <div class="contact">
      <h1 class="person-name">Daniel Hartley</h1>
      <p class="person-role">President</p>
      <ul class="contact-list">
        <li>03 5821 6094
          <svg viewBox="0 0 24 24" fill="var(--orange)"><path d="M6.6 10.8a15.1 15.1 0 0 0 6.6 6.6l2.2-2.2c.3-.3.7-.4 1-.2 1.1.4 2.3.6 3.6.6.6 0 1 .4 1 1V20c0 .6-.4 1-1 1A17 17 0 0 1 3 4c0-.6.4-1 1-1h3.5c.6 0 1 .4 1 1 0 1.3.2 2.5.6 3.6.1.3 0 .7-.2 1z"/></svg>
        </li>
        <li>office@brackleyearthworks.com.au
          <svg viewBox="0 0 24 24" fill="var(--orange)"><path d="M2 5h20v14H2z"/><path d="M2 5l10 8 10-8" fill="none" stroke="#1d1d1e" stroke-width="2"/></svg>
        </li>
        <li>brackleyearthworks.com.au
          <svg viewBox="0 0 24 24"><circle cx="12" cy="12" r="10" fill="var(--orange)"/><path d="M2 12h20M12 2c3 3 3 17 0 20M12 2c-3 3-3 17 0 20" fill="none" stroke="#1d1d1e" stroke-width="1.6"/></svg>
        </li>
        <li>42 Kellaway Road, Tarrawong
          <svg viewBox="0 0 24 24" fill="var(--orange)"><path d="M12 2a7 7 0 0 0-7 7c0 5 7 13 7 13s7-8 7-13a7 7 0 0 0-7-7zm0 9.5A2.5 2.5 0 1 1 12 6.5a2.5 2.5 0 0 1 0 5z"/></svg>
        </li>
        <li class="no-icon">Victoria 3728, Australia</li>
      </ul>
    </div>
  </section>

</body>
</html>
```